interior designer/stylist looking for a letter press business card to reflect the stylish work

Hello Designers,
I need a business card design for an company called Halvern Interior Design. I'm aiming at the high end residential and private client market in London providing sleek simple interiors. I'd like my business card to be snipboard worthy and expensive looking, i want people to pin it and for it to have a sought after look, and want prospective customers to hire me as their interior designer as my card is so beautiful.
I love letter press design. I also like the use of colour/foil on the edge.
Colour combos & general things I like -
Black and White
Navy Blue and Gold
Neutral colours (muted palette of greys whites navys beiges)
White Marble & brass
Vaubris (fashion designer)
....also open to other suggestions....
Please dont take the pink in the attached photos too literally. i'd like the card to look more masculine than feminine.
I'd like Halvern on one side in one font, with interior design underneath so one word will make the statement....... unless anyone has any other ideas, open to suggestions.
I'd like a really simple font and for the whole card to look very graphic.
my details -
Maren Oakcliffe
Interior Designer & Stylist
email maren@halverninteriordesign.co.uk
phone +447813550296
website wwww.halverninteriordesign.co.uk
GO GO GO!! EXCITED TO SEE THE OUTCOME!!
x M
Target Market(s)
High End Residential and private clients
Industry/Entity Type
Business
Contact Information for Business Card
Halvern Interior Design & Styling
Maren Oakcliffe
phone +447813550296

```html
<!DOCTYPE html>
<html lang="en">
<head>
<meta charset="utf-8">
<title>Halvern Interior Design – Business Cards</title>
<link rel="stylesheet" href="https://fonts.googleapis.com/css2?family=Mulish:wght@300;400&display=swap">
<style>
  :root {
    --page: #ffffff;
    --stock: #ececec;
    --gold: #857a5a;
    --navy: #20213f;
    --navy-ink: #22224a;
    --slate: #555555;
    --graphite: #4f4f4f;
    --navy-faint: #363259;
    --slate-faint: #6c6c6c;
    --white: #ffffff;
  }
  * { box-sizing: border-box; margin: 0; padding: 0; }
  html, body {
    width: 1200px; height: 782px; overflow: hidden;
    background: var(--page);
    font-family: "Mulish", "Avenir", sans-serif;
    font-weight: 300;
  }
  .sheet { position: relative; width: 1200px; height: 782px; }
  .card {
    position: absolute;
    width: 568px; height: 367px;
    border: 2px solid var(--gold);
    border-radius: 24px;
    overflow: hidden;
  }
  .card--front { background: var(--stock); top: 2px; }
  .card--back { top: 414px; }
  .card--left { left: 2px; }
  .card--right { left: 631px; }
  .card--navy { background: var(--navy); }
  .card--slate { background: var(--slate); }

  .wordmark {
    position: absolute; left: 0; right: 0; top: 118px;
    text-align: center;
    font-size: 78px; font-weight: 300; line-height: 1;
    letter-spacing: 0.04em;
  }
  .card--left .wordmark { color: var(--gold); }
  .card--right .wordmark { color: var(--graphite); }
  .tagline {
    position: absolute; left: 0; right: 0; top: 258px;
    text-align: center;
    font-size: 17px; font-weight: 400;
    letter-spacing: 0.3em;
  }
  .card--left .tagline { color: var(--navy-ink); }
  .card--right .tagline { color: var(--gold); }

  .brand-watermark {
    position: absolute; left: 232px; top: 140px;
    font-size: 96px; font-weight: 400; line-height: 1;
  }
  .card--navy .brand-watermark { color: var(--navy-faint); }
  .card--slate .brand-watermark { color: var(--slate-faint); }

  .person { position: absolute; left: 40px; top: 46px; }
  .person__name { color: var(--white); font-size: 32px; font-weight: 300; line-height: 1.2; }
  .person__role { color: var(--gold); font-size: 18px; font-weight: 300; margin-top: 4px; }

  .contacts { position: absolute; left: 40px; top: 256px; list-style: none; }
  .contacts li { display: flex; height: 28px; align-items: center; font-size: 18px; }
  .contacts .label { color: var(--white); width: 26px; }
  .contacts .value { color: var(--gold); }
</style>
</head>
<body>
<main class="sheet">
  <section class="card card--front card--left">
    <div class="wordmark">Halvern</div>
    <div class="tagline">Halvern Interior Design</div>
  </section>
  <section class="card card--front card--right">
    <div class="wordmark">Halvern</div>
    <div class="tagline">Halvern Interior Design</div>
  </section>

  <section class="card card--back card--left card--navy">
    <div class="brand-watermark" aria-hidden="true">Halvern</div>
    <div class="person">
      <h1 class="person__name">Maren Oakcliffe</h1>
      <p class="person__role">Interior Designer &amp; Stylist</p>
    </div>
    <ul class="contacts">
      <li><span class="label">e</span><span class="value">maren@halverninteriordesign.co.uk</span></li>
      <li><span class="label">t</span><span class="value">+44 (0)781 355 0296</span></li>
      <li><span class="label">w</span><span class="value">wwww.halverninteriordesign.co.uk</span></li>
    </ul>
  </section>
  <section class="card card--back card--right card--slate">
    <div class="brand-watermark" aria-hidden="true">Halvern</div>
    <div class="person">
      <h2 class="person__name">Maren Oakcliffe</h2>
      <p class="person__role">Interior Designer &amp; Stylist</p>
    </div>
    <ul class="contacts">
      <li><span class="label">e</span><span class="value">maren@halverninteriordesign.co.uk</span></li>
      <li><span class="label">t</span><span class="value">+44 (0)781 355 0296</span></li>
      <li><span class="label">w</span><span class="value">wwww.halverninteriordesign.co.uk</span></li>
    </ul>
  </section>
</main>
</body>
</html>
```